Menu Board and Flyer for a Poke Restaurant

We need for our new Menu board for a Poke restaurant. There will be 2 separate boards. 1 Board for Speciality items, the second for "Build your Own". The menu boards will be installed on a wall.

The first board is going to be 36 W x 48 H inches. The second board will be 72 W x 48 H inches.

I would also like to consolidate the board into a one Page menu flyer that can be printed on an 11 inches x 14 inches Page.

The goal is to have customers focus on the ease of ordering.
We have attached a sample design idea for reference and our logo options. Including the logo is optional.

I have included some sample menus by other companies as attachment and referance.

Files need to include any special fonts used in the design.

Target Market(s)

Young Professionals who love eating healthy, trendy, delicious new food options.

Industry/Entity Type

Fast Food Restaurant

Font styles to use
Serif
Sans Serif

Requirements
Must have
• Simple
• Clean design - NOT busy
• Fun
• Easy to follow
• Highlight a step by step ordering process.
• Light background color
• Files need to include any special fonts used in the design.
Should not have
• script fonts

```html
<!DOCTYPE html>
<html lang="en">
<head>
<meta charset="utf-8">
<title>House Specialities Menu</title>
<link href="https://fonts.googleapis.com/css2?family=Staatliches&family=Hind:wght@400;500&display=swap" rel="stylesheet">
<style>
  :root {
    --paper: #ffffff;
    --ink: #1c1c1c;
    --step-grey: #d0d0d0;
    --name-grey: #bdbdbd;
  }
  * { margin: 0; padding: 0; box-sizing: border-box; }
  html, body { width: 900px; height: 1200px; overflow: hidden; background: var(--paper); }
  .menu {
    position: relative;
    width: 900px;
    height: 1200px;
    background: var(--paper);
    color: var(--ink);
    font-family: "Hind", sans-serif;
  }
  .menu-title {
    position: absolute;
    top: 48px; left: 0; width: 900px;
    text-align: center;
    font-family: "Staatliches", sans-serif;
    font-weight: 400;
    font-size: 41px;
    line-height: 44px;
    letter-spacing: 1px;
  }
  .step {
    position: absolute;
    top: 211px;
    width: 260px;
    height: 64px;
  }
  .step-number {
    position: absolute;
    left: 0; top: 0;
    width: 32px; height: 64px;
    background: var(--step-grey);
    color: var(--paper);
    font-size: 24px;
    line-height: 68px;
    text-align: center;
  }
  .step-lead {
    position: absolute;
    left: 44px; top: 3px;
    font-size: 19px;
    line-height: 21px;
    font-weight: 500;
  }
  .step-name {
    position: absolute;
    left: 44px; top: 26px;
    font-family: "Staatliches", sans-serif;
    font-size: 38px;
    line-height: 40px;
    letter-spacing: 2px;
  }
  .step-speciality { left: 50px; }
  .step-style { left: 317px; }
  .step-base { left: 583px; }

  .option-list { position: absolute; top: 0; list-style: none; }
  .col-speciality { left: 94px; }
  .col-style { left: 361px; }
  .col-base { left: 627px; }
  .option {
    position: absolute;
    left: 0;
    white-space: nowrap;
  }
  .option-name {
    display: block;
    font-size: 27px;
    line-height: 30px;
    font-weight: 500;
  }
  .option-note {
    display: block;
    font-size: 19.5px;
    line-height: 27px;
    margin-top: 5px;
  }
  .brand-name {
    position: absolute;
    left: 627px; top: 1040px;
    color: var(--name-grey);
    font-size: 24px;
    line-height: 28px;
    font-weight: 500;
    white-space: nowrap;
  }
</style>
</head>
<body>
<main class="menu">
  <h1 class="menu-title">House Specialities</h1>

  <div class="step step-speciality">
    <span class="step-number">1</span>
    <span class="step-lead">Choose a</span>
    <span class="step-name">Speciality</span>
  </div>
  <div class="step step-style">
    <span class="step-number">2</span>
    <span class="step-lead">Choose your</span>
    <span class="step-name">Style</span>
  </div>
  <div class="step step-base">
    <span class="step-number">3</span>
    <span class="step-lead">Choose your</span>
    <span class="step-name">Base</span>
  </div>

  <ul class="option-list col-speciality">
    <li class="option" style="top:368px"><span class="option-name">Lava Hot</span></li>
    <li class="option" style="top:502px"><span class="option-name">Classic Hawaiian</span></li>
    <li class="option" style="top:635px"><span class="option-name">Sweet &amp; Spicy</span></li>
    <li class="option" style="top:777px"><span class="option-name">Crazy Kimchi</span></li>
    <li class="option" style="top:917px"><span class="option-name">Wasabi Lover</span></li>
    <li class="option" style="top:1050px"><span class="option-name">Ginger Ginger</span></li>
  </ul>

  <ul class="option-list col-style">
    <li class="option" style="top:368px">
      <span class="option-name">Classic Bowl</span>
      <span class="option-note">( Regular or Large )</span>
    </li>
    <li class="option" style="top:502px">
      <span class="option-name">Crunchy Bowl</span>
      <span class="option-note" style="margin-top:13px">( One size, Tostada style )</span>
    </li>
    <li class="option" style="top:635px">
      <span class="option-name">Surfer Style</span>
      <span class="option-note" style="margin-top:13px">( Poke served Taco Style )</span>
    </li>
    <li class="option" style="top:777px">
      <span class="option-name">Just Poke ( 1Lb )</span>
      <span class="option-note">( No base -<br>1lb of your favourite poke )</span>
    </li>
  </ul>

  <ul class="option-list col-base">
    <li class="option" style="top:368px"><span class="option-name">White Rice</span></li>
    <li class="option" style="top:502px"><span class="option-name">Brown Rice</span></li>
    <li class="option" style="top:635px"><span class="option-name">Black Rice</span></li>
    <li class="option" style="top:777px"><span class="option-name">Mixed Greens</span></li>
  </ul>

  <p class="brand-name">Marlow Fish Bar</p>
</main>
</body>
</html>
```